Design and Renovation Company Luxury Business Card

I want to create a luxury business card for a Design and Renovation Firm . We will use our current logo. The company name is 742KAVO. We do not want anything standard. We need a very unique concept.
Please see uploaded inspiration. I really like the textured paper option. I would like the card to be thick with debossing, and/or embossing options. The logo has orange in it but I would like to see the card with and without the orange. I think the orange may make the company feel less high-end. The goal is to elevate the logo not match its vibe per se of the logo. We want something very unique, not standard at all!
I would like a space for :
Logo,
Name,
Position,
Email,
Office number,
Website Address,
Business Address,
Thank you!
Have fun!
Target Market(s)
Home owners Age 35 +
Industry/Entity Type
Design and Renovation
Contact Information for Business Card
Logo, Name, Position, Email, Office number, Website Address, Business Address,.
Colors
Designer to choose colors to be used in the design.
Requirements
Must have
- A luxury designer feel. Must be black or dark grey but open to other luxury ideas.
Nice to have
- Gold, silver, black embossing or debossing. Textured paper design.
Should not have
- A cheap look and feel.

```html
<!DOCTYPE html>
<html lang="en">
<head>
<meta charset="UTF-8">
<title>742KAVO Business Card</title>
<link href="https://fonts.googleapis.com/css2?family=Roboto:wght@400;500&display=swap" rel="stylesheet">
<style>
  :root {
    --backdrop: #e9e8e6;
    --card: #1f201f;
    --gold: #c9a26b;
    --gold-soft: #b8935f;
    --ink-on-gold: #1f201f;
  }
  * { margin: 0; padding: 0; box-sizing: border-box; }
  html, body {
    width: 1200px;
    height: 745px;
    overflow: hidden;
    background: var(--backdrop);
    font-family: "Roboto", Arial, sans-serif;
  }
  .canvas {
    position: relative;
    width: 1200px;
    height: 745px;
  }
  .card {
    position: absolute;
    top: 224px;
    width: 517px;
    height: 298px;
    background: var(--card);
    color: var(--gold);
  }
  .card--front { left: 50px; }
  .card--back { left: 598px; }

  .brand-name {
    position: absolute;
    transform: translate(-50%, -50%);
    font-weight: 400;
    color: var(--gold);
    letter-spacing: 0.02em;
    white-space: nowrap;
    line-height: 1;
  }
  .card--front .brand-name { left: 50%; top: 50%; font-size: 46px; }
  .card--back .brand-name { left: 133px; top: 149px; font-size: 30px; }

  .divider {
    position: absolute;
    left: 257px;
    top: 39px;
    width: 2px;
    height: 235px;
    background: var(--gold-soft);
  }

  .identity {
    position: absolute;
    left: 295px;
    top: 36px;
    width: 134px;
    text-align: right;
  }
  .identity__name {
    font-size: 22px;
    font-weight: 500;
    line-height: 1.1;
    letter-spacing: -0.01em;
    white-space: nowrap;
  }
  .identity__position {
    font-size: 13px;
    font-weight: 400;
    margin-top: 3px;
  }

  .contacts {
    position: absolute;
    left: 295px;
    top: 127px;
    list-style: none;
  }
  .contacts__item {
    display: flex;
    align-items: center;
    height: 18px;
    margin-bottom: 8.7px;
    font-size: 13px;
  }
  .contacts__icon {
    width: 18px;
    height: 18px;
    margin-right: 17px;
    flex: none;
  }
</style>
</head>
<body>
<main class="canvas">
  <section class="card card--front" aria-label="Card front">
    <div class="brand-name">742KAVO</div>
  </section>

  <section class="card card--back" aria-label="Card back">
    <div class="brand-name">742KAVO</div>
    <div class="divider"></div>

    <div class="identity">
      <div class="identity__name">YOUR NAME</div>
      <div class="identity__position">Your Position</div>
    </div>

    <ul class="contacts">
      <li class="contacts__item">
        <svg class="contacts__icon" viewBox="0 0 18 18" aria-hidden="true">
          <rect width="18" height="18" fill="var(--gold)"/>
          <path d="M9 3.5a3.6 3.6 0 0 0-3.6 3.6C5.4 10 9 14.5 9 14.5s3.6-4.5 3.6-7.4A3.6 3.6 0 0 0 9 3.5z" fill="none" stroke="var(--ink-on-gold)" stroke-width="1.2"/>
          <circle cx="9" cy="7.2" r="1.3" fill="var(--ink-on-gold)"/>
        </svg>
        <span>Business Address</span>
      </li>
      <li class="contacts__item">
        <svg class="contacts__icon" viewBox="0 0 18 18" aria-hidden="true">
          <rect width="18" height="18" fill="var(--gold)"/>
          <path d="M5 3.5l2.2-.3 1.2 3-1.4 1.1a7 7 0 0 0 3.6 3.6l1.1-1.4 3 1.2-.3 2.2c-.2.8-1 1.3-1.8 1.2C7.8 13.6 4.4 10.2 3.8 5.4c-.1-.8.4-1.6 1.2-1.9z" fill="var(--ink-on-gold)"/>
        </svg>
        <span>Office number</span>
      </li>
      <li class="contacts__item">
        <svg class="contacts__icon" viewBox="0 0 18 18" aria-hidden="true">
          <rect width="18" height="18" fill="var(--gold)"/>
          <rect x="3.5" y="5" width="11" height="8" fill="none" stroke="var(--ink-on-gold)" stroke-width="1.1"/>
          <path d="M3.5 5L9 9.7 14.5 5M3.5 13l4-3.6M14.5 13l-4-3.6" fill="none" stroke="var(--ink-on-gold)" stroke-width="1.1"/>
        </svg>
        <span>Email</span>
      </li>
      <li class="contacts__item">
        <svg class="contacts__icon" viewBox="0 0 18 18" aria-hidden="true">
          <rect width="18" height="18" fill="var(--gold)"/>
          <circle cx="9" cy="9" r="5.2" fill="none" stroke="var(--ink-on-gold)" stroke-width="1"/>
          <ellipse cx="9" cy="9" rx="2.3" ry="5.2" fill="none" stroke="var(--ink-on-gold)" stroke-width="1"/>
          <path d="M3.8 9h10.4M4.6 6.4h8.8M4.6 11.6h8.8" stroke="var(--ink-on-gold)" stroke-width="0.9"/>
        </svg>
        <span>Website Address</span>
      </li>
    </ul>
  </section>
</main>
</body>
</html>
```